plovu business card design

plovu is an incubator within RTM Media focused on unlocking the potential in underserved niche micro-verticals on the web. our mission is to rapidly develop and foster emerging micro-verticals bc they are ripe for growth - building interesting and trusted content experiences with unqiue, useful and cutting-edge delivery methods.please do all copy (except for RTM Media, which must look as typed here and in logo) in all lowercase. Also please use spaces between phone # extensions not dashes or periods. I have attached all variations of the logo.
Industry/Entity Type
Business
Contact Information for Business Card
daria feltow, ceo www.plovu.io 218 holbrook lane 3rd floor oakland ca 94731 415 602 0002m 510 985 7966d daria.feltow@plovu.io
Look and feel
Each slider illustrates characteristics of the customer's brand and the style your logo design should communicate.

```html
<!DOCTYPE html>
<html lang="en">
<head>
<meta charset="utf-8">
<title>plovu business card</title>
<link href="https://fonts.googleapis.com/css2?family=Open+Sans:wght@400;600;700&display=swap" rel="stylesheet">
<style>
  :root {
    --stage: #2b2b2b;
    --ink-black: #0e0e0e;
    --paper: #ffffff;
    --teal: #1f9490;
    --charcoal: #1a1a1a;
    --text-grey: #555555;
    --text-dark: #111111;
  }
  * { margin: 0; padding: 0; box-sizing: border-box; }
  html, body { width: 1200px; height: 900px; overflow: hidden; }
  body {
    background: var(--stage);
    font-family: "Open Sans", Arial, sans-serif;
    position: relative;
  }
  .card {
    position: absolute;
    left: 300px;
    width: 600px;
    height: 343px;
    overflow: hidden;
  }
  .card--back { top: 88px; background: var(--ink-black); }
  .card--front { top: 469px; background: var(--paper); }

  .brand { position: absolute; }
  .brand__name {
    display: flex;
    align-items: center;
    font-weight: 700;
    line-height: 1.3;
    letter-spacing: -2px;
  }
  .brand__dot { border-radius: 50%; background: var(--teal); flex: none; }
  .brand__tagline { font-weight: 400; letter-spacing: 0.5px; line-height: 1.2; }

  .card--back .brand { left: 50px; top: 40px; color: var(--paper); }
  .card--back .brand__name { font-size: 140px; gap: 14px; }
  .card--back .brand__dot { width: 32px; height: 32px; margin-top: 18px; }
  .card--back .brand__tagline { font-size: 24px; margin-top: 2px; padding-left: 4px; }

  .card--front .brand { left: 40px; top: 100px; color: var(--text-dark); }
  .card--front .brand__name { font-size: 78px; letter-spacing: -1px; gap: 10px; }
  .card--front .brand__dot { width: 18px; height: 18px; margin-top: 8px; }
  .card--front .brand__tagline { font-size: 14px; margin-top: 2px; padding-left: 3px; }

  .divider {
    position: absolute;
    left: 300px; top: 24px;
    width: 2px; height: 120px;
    background: linear-gradient(to bottom, var(--teal), rgba(31,148,144,0));
    transform: rotate(-14deg);
    transform-origin: top;
  }
  .contact {
    position: absolute;
    left: 345px; top: 24px;
    color: var(--text-grey);
    font-size: 13px;
    line-height: 1.35;
  }
  .contact__name { color: var(--teal); font-weight: 700; font-size: 15px; }
  .contact__role { margin-bottom: 8px; }
  .contact__list { list-style: none; margin-top: 6px; }
  .contact__list li { display: flex; align-items: center; gap: 10px; margin-bottom: 2px; }
  .contact__list svg { width: 12px; height: 12px; fill: var(--teal); flex: none; }
  .swoosh { position: absolute; left: 0; bottom: 0; width: 600px; height: 343px; }
</style>
</head>
<body>
  <section class="card card--back">
    <div class="brand">
      <div class="brand__name">plovu<span class="brand__dot"></span></div>
      <div class="brand__tagline">an RTM Media incubator</div>
    </div>
  </section>

  <section class="card card--front">
    <svg class="swoosh" viewBox="0 0 600 343" aria-hidden="true">
      <path d="M600 170 C 470 250 280 300 0 318 L0 343 L600 343 Z" fill="var(--charcoal)"/>
      <path d="M0 300 C 240 308 430 280 600 240 C 430 290 250 320 0 322 Z" fill="var(--teal)"/>
      <path d="M0 322 C 250 320 430 290 600 240 L600 250 C 430 298 250 330 0 330 Z" fill="var(--paper)"/>
    </svg>
    <div class="brand">
      <div class="brand__name">plovu<span class="brand__dot"></span></div>
      <div class="brand__tagline">an RTM Media incubator</div>
    </div>
    <div class="divider"></div>
    <div class="contact">
      <div class="contact__name">daria feltow</div>
      <div class="contact__role">C.E.O</div>
      <div>218 holbrook lane 3rd floor</div>
      <div>oakland ca 94731</div>
      <ul class="contact__list">
        <li><svg viewBox="0 0 24 24"><path d="M6.6 10.8a15.1 15.1 0 0 0 6.6 6.6l2.2-2.2a1 1 0 0 1 1-.25 11.4 11.4 0 0 0 3.6.57 1 1 0 0 1 1 1V20a1 1 0 0 1-1 1A17 17 0 0 1 3 4a1 1 0 0 1 1-1h3.5a1 1 0 0 1 1 1c0 1.25.2 2.45.57 3.57a1 1 0 0 1-.25 1z"/></svg>415 738 4196</li>
        <li><svg viewBox="0 0 24 24"><path d="M12 2a10 10 0 1 0 0 20 10 10 0 0 0 0-20zm6.9 6h-2.9a15.6 15.6 0 0 0-1.4-3.6A8 8 0 0 1 18.9 8zM12 4c.8 1.2 1.5 2.5 1.9 4h-3.8c.4-1.5 1.1-2.8 1.9-4zM4.3 14a8 8 0 0 1 0-4h3.4a16 16 0 0 0 0 4zm.8 2h2.9c.3 1.3.8 2.5 1.4 3.6A8 8 0 0 1 5.1 16zM8 8H5.1a8 8 0 0 1 4.3-3.6C8.8 5.5 8.3 6.7 8 8zm4 12c-.8-1.2-1.5-2.5-1.9-4h3.8c-.4 1.5-1.1 2.8-1.9 4zm2.3-6H9.7a14.6 14.6 0 0 1 0-4h4.6a14.6 14.6 0 0 1 0 4zm.3 5.6c.6-1.1 1.1-2.3 1.4-3.6h2.9a8 8 0 0 1-4.3 3.6zm1.7-5.6a16 16 0 0 0 0-4h3.4a8 8 0 0 1 0 4z"/></svg>www.plovu.io</li>
        <li><svg viewBox="0 0 24 24"><path d="M12 2a10 10 0 0 0 0 20h5v-2h-5a8 8 0 1 1 8-8v1.4c0 .8-.7 1.6-1.5 1.6S17 14.2 17 13.4V12a5 5 0 1 0-1.5 3.5A3.5 3.5 0 0 0 22 13.4V12A10 10 0 0 0 12 2zm0 13a3 3 0 1 1 0-6 3 3 0 0 1 0 6z"/></svg>daria.feltow@plovu.io</li>
      </ul>
    </div>
  </section>
</body>
</html>
```